Fresh Start Body Quest 2017 Poster

We are having a Fresh Start, Body Quest for 2017 at our fitness studio. We need a poster design using the template attached as a reference (Only reference). I have also included our Drovelux logo to put on the poster. Please DO NOT use the graphics in the flyer as we are expecting something much much better :-)
MUST HAVES:
- Size needed 11x17 with bleeding for printing
- .PSD File Format WITH LAYERS (CS3 Compatible)*** A MUST
- Use Drovelux Bootcamps Logo
- Use Information in the attached word doc

```html
<!DOCTYPE html>
<html lang="en">
<head>
<meta charset="utf-8">
<title>Fresh Start, Body Quest 2017 – Drovelux Bootcamps</title>
<link rel="stylesheet" href="https://fonts.googleapis.com/css2?family=Oswald:wght@400;500;600&family=Roboto+Condensed:wght@400;700&display=swap">
<style>
  :root {
    --charcoal: #3a3a3d;
    --charcoal-deep: #2b2b2e;
    --slate: #4a4a4e;
    --turf: #2f9a45;
    --brand-blue: #4a8fd8;
    --accent-orange: #f08a24;
    --ink: #1c1c1e;
    --paper: #ffffff;
    --muted: #e6e6e6;
  }
  * { box-sizing: border-box; margin: 0; padding: 0; }
  html, body { width: 914px; height: 1200px; overflow: hidden; background: var(--paper); }
  .poster {
    position: relative; width: 914px; height: 1200px; overflow: hidden;
    background: var(--charcoal);
    font-family: "Roboto Condensed", "Arial Narrow", sans-serif;
    color: var(--paper);
  }
  .brand-plate {
    position: absolute; left: 267px; top: 40px; width: 380px; height: 140px;
    background: var(--paper); border: 6px solid var(--ink); border-radius: 8px;
    display: flex; align-items: center; justify-content: center;
  }
  .brand-name {
    font-family: "Oswald", sans-serif; font-weight: 600; font-size: 34px;
    color: var(--charcoal-deep); text-transform: uppercase; letter-spacing: 1px;
    white-space: nowrap;
  }
  .headline {
    position: absolute; left: 0; right: 0; top: 205px; text-align: center;
    font-family: "Oswald", sans-serif; font-weight: 500; text-transform: uppercase;
  }
  .headline-main { display: block; font-size: 86px; line-height: 1.05; }
  .headline-sub { display: block; font-size: 46px; line-height: 1.1; }
  .promise-band {
    position: absolute; left: 0; top: 395px; width: 100%; height: 112px;
    background: var(--brand-blue); text-align: center; padding-top: 14px;
    z-index: 2;
  }
  .promise-line { font-size: 36px; line-height: 1.2; white-space: nowrap; }
  .promise-line.strong { font-weight: 700; font-size: 32px; }
  .promise-pointer { position: absolute; right: 110px; bottom: -22px; }
  .training-photo {
    position: absolute; left: 0; top: 507px; width: 100%; height: 591px;
    background: linear-gradient(180deg, var(--slate) 0%, var(--charcoal-deep) 58%, #1f5f2c 78%, var(--turf) 100%);
  }
  .kickoff { position: absolute; right: 38px; top: 565px; text-align: right; }
  .kickoff-title {
    font-family: "Oswald", sans-serif; font-weight: 500; font-size: 48px;
    color: var(--accent-orange); line-height: 1.1;
  }
  .event-detail { font-size: 26px; color: var(--muted); white-space: nowrap; }
  .rule { position: absolute; height: 3px; background: var(--accent-orange); }
  .rule.top { left: 40px; right: 360px; top: 640px; }
  .rule.bottom { left: 560px; right: 38px; top: 700px; }
  .schedule {
    position: absolute; left: 40px; top: 660px; right: 38px;
    display: flex; align-items: flex-start;
  }
  .schedule-item { padding: 0 22px; border-left: 3px solid var(--muted); }
  .schedule-item:first-child { padding-left: 0; border-left: none; }
  .schedule-item.end { margin-top: 20px; }
  .schedule-item.finale { margin-top: 58px; }
  .schedule-label {
    font-family: "Oswald", sans-serif; font-weight: 500; font-size: 26px;
    color: var(--accent-orange); text-transform: uppercase;
  }
  .prize-badge {
    position: absolute; left: 40px; top: 760px; width: 230px; height: 230px;
    border-radius: 50%; background: var(--brand-blue); color: var(--ink);
    display: flex; flex-direction: column; align-items: center; justify-content: center;
    font-family: "Oswald", sans-serif; font-weight: 500; text-align: center; line-height: 1.05;
  }
  .prize-amount { font-size: 52px; color: var(--paper); }
  .prize-text { font-size: 34px; }
  .prize-winner { font-size: 48px; }
  .offer-band {
    position: absolute; left: 0; top: 1030px; width: 810px; height: 68px;
    background: var(--brand-blue);
    clip-path: polygon(0 0, 95% 0, 100% 100%, 0 100%);
    font-family: "Oswald", sans-serif; font-size: 25px; line-height: 68px;
    padding-left: 22px; white-space: nowrap;
  }
  .footer {
    position: absolute; left: 0; bottom: 0; width: 100%; height: 102px;
    background: var(--paper); color: var(--ink);
    display: flex; align-items: center; justify-content: center;
    font-family: "Oswald", sans-serif; font-size: 38px; font-weight: 400;
    white-space: nowrap;
  }
  .footer-url { color: var(--brand-blue); margin: 0 10px; font-weight: 500; }
</style>
</head>
<body>
<main class="poster">
  <div class="brand-plate"><span class="brand-name">Drovelux Bootcamps</span></div>

  <h1 class="headline">
    <span class="headline-main">Fresh Start,</span>
    <span class="headline-sub">Body Quest</span>
  </h1>

  <div class="training-photo" role="img" aria-label="Woman doing a push-up on two blue kettlebells on green gym turf"></div>

  <div class="promise-band">
    <p class="promise-line">In Just 6 Weeks, Transform Your Body And Get In</p>
    <p class="promise-line strong">The Best Shape Of Your Life!</p>
    <svg class="promise-pointer" width="34" height="24" viewBox="0 0 34 24" aria-hidden="true">
      <polygon points="0,0 34,0 17,24" fill="var(--brand-blue)"/>
    </svg>
  </div>

  <div class="kickoff">
    <p class="kickoff-title">Kick Off Meeting:</p>
    <p class="event-detail">Thursday, Jan 12th at 7:30 pm</p>
  </div>
  <div class="rule top"></div>
  <div class="rule bottom"></div>

  <div class="schedule">
    <div class="schedule-item start">
      <p class="schedule-label">Start Date:</p>
      <p class="event-detail">Tuesday, January 17th</p>
    </div>
    <div class="schedule-item end">
      <p class="schedule-label">End Date:</p>
      <p class="event-detail">Saturday, February 25th</p>
    </div>
    <div class="schedule-item finale">
      <p class="schedule-label">Finale Party</p>
      <p class="event-detail">March 2nd</p>
    </div>
  </div>

  <div class="prize-badge">
    <span class="prize-amount">$500</span>
    <span class="prize-text">CASH Prize</span>
    <span class="prize-text">for</span>
    <span class="prize-winner">Winner!</span>
  </div>

  <div class="offer-band">6 Weeks of Training, Nutrition, and Coaching Starting at just $99!</div>

  <footer class="footer">
    Visit <span class="footer-url">WWW.DROVELUXBOOTCAMPS.COM</span> For More Info
  </footer>
</main>
</body>
</html>
```